Arzt im ästhetischen Bereich sucht seriöses Flyer-Design
Zielgruppe
Ich bin Arzt und nebenberuflich mache ich Eingriffe im ästhetischen Bereich (Lumex- und Hyaluronunterspritzung, Lipolyse, Eigenblutbehandlung (PRP) bzw. Perlglanzkur).
Ich möchte gerne einen sechsseitigen Flyer mit Falz. Auf der Deckseite sollte ein schönes Logo mit ästhetischen Bezug stehen, auf den anderen Seiten werden je die Behandlungsmethoden erklärt (Text kann ich zusteuern bzw. füge ich nach Erhalt des Designs ein). Es sollten auf jeder Seite schöne Abbildungen (entweder Fotomaterial oder auch Zeichnungen) der Methoden enthalten sein. Auf der letzten Seite sollen meine Kontaktdaten stehen
Aufgabenstellung
s.o. 6 seitiger Flyer mit Falzen. Farbe frei. Design medizinisch-ästhetisch mit seriösen Eindruck. Logo von mir soll auf der Rückseite mit meinen Kontaktdaten eingefügt werden.

```html
<!DOCTYPE html>
<html lang="de">
<head>
<meta charset="utf-8">
<title>Flyer Hyaluron und Lumex</title>
<link rel="stylesheet" href="https://fonts.googleapis.com/css2?family=Raleway:wght@400;500;700&display=swap">
<style>
  :root {
    --stage: #e9ecef;
    --paper: #ffffff;
    --sky: #45b0e0;
    --ink: #2e4a5c;
    --heading: #2b4658;
    --wave-dark: #2b5264;
    --wave-light: #82c9e9;
    --skin: #ecc9b9;
    --glove: #6fbfe6;
  }
  html, body {
    margin: 0;
    padding: 0;
    width: 1200px;
    height: 676px;
    overflow: hidden;
    background: var(--stage);
  }
  .flyer {
    position: absolute;
    left: 136px;
    top: 10px;
    width: 1414px;
    height: 999px;
    background: var(--paper);
    transform: scale(0.656);
    transform-origin: top left;
    overflow: hidden;
    font-family: 'Raleway', sans-serif;
    color: var(--ink);
  }
  .top-band {
    position: absolute;
    left: 0; top: 0;
    width: 1414px; height: 32px;
    background: var(--sky);
  }
  .photo-lips {
    position: absolute;
    left: 0; top: 32px;
    width: 909px; height: 419px;
    background: linear-gradient(100deg, var(--skin) 0%, #f1d6c9 38%, #f7e8e1 55%, #ffffff 68%, #cfe9f6 82%, var(--glove) 100%);
  }
  .photo-eye {
    position: absolute;
    left: 966px; top: 32px;
    width: 448px; height: 446px;
    background:
      linear-gradient(to bottom, rgba(255,255,255,0) 55%, #ffffff 100%),
      linear-gradient(90deg, #e2c0ae 0%, #d6b5a4 45%, #9cc4da 75%, #4f9fd1 100%);
  }
  .heading {
    position: absolute;
    margin: 0;
    font-size: 24px;
    font-weight: 700;
    color: var(--heading);
    text-decoration: underline;
    text-underline-offset: 3px;
    text-decoration-thickness: 2px;
  }
  .heading--hyaluron { left: 32px; top: 460px; }
  .heading--lumex { left: 969px; top: 493px; }
  .text-col {
    position: absolute;
    width: 430px;
    font-size: 16.6px;
    line-height: 20.1px;
    font-weight: 500;
  }
  .text-col p { margin: 0 0 20px; }
  .text-col--one { left: 33px; top: 518px; }
  .text-col--two { left: 509px; top: 518px; }
  .text-col--three { left: 969px; top: 547px; width: 420px; }
  .wave {
    position: absolute;
    left: 0; top: 0;
    width: 1414px; height: 999px;
  }
  .footer-claim {
    position: absolute;
    left: 0; top: 924px;
    width: 1414px;
    text-align: center;
    color: #ffffff;
    font-weight: 700;
    font-size: 22px;
    line-height: 27px;
  }
  .footer-claim p { margin: 0; }
</style>
</head>
<body>
  <div class="flyer">
    <div class="top-band"></div>
    <div class="photo-lips" role="img" aria-label="Foto: Hyaluron-Injektion an den Lippen, Hände in blauen Handschuhen mit Spritze"></div>
    <div class="photo-eye" role="img" aria-label="Foto: Lumex-Injektion neben dem Auge, Hände in blauen Handschuhen"></div>

    <svg class="wave" viewBox="0 0 1414 999" aria-hidden="true">
      <defs>
        <linearGradient id="waveFill" x1="0" y1="0" x2="1" y2="0">
          <stop offset="0" stop-color="var(--wave-dark)"/>
          <stop offset="0.5" stop-color="#3f7389"/>
          <stop offset="1" stop-color="var(--wave-light)"/>
        </linearGradient>
      </defs>
      <path d="M0 680 C 120 790, 420 860, 800 880 C 1050 893, 1250 900, 1414 905 L1414 999 L0 999 Z" fill="url(#waveFill)"/>
    </svg>

    <h2 class="heading heading--hyaluron">Hyaluron-Behandlung</h2>
    <div class="text-col text-col--one">
      <p>Hyaluron ist ein wichtiger Bestandteil des Binde-<br>gewebes und auch für die Zellfunktion notwendig.<br>Weiterhin ist Hyaluron für die Wasserspeicherung<br>und somit Elastizität der Haut entscheidend. Größere<br>und tiefere Falten, bei denen eine Lumex-Behand-<br>lung nicht sinnvoll bzw. nicht möglich erscheint,<br>eignen sich hervorragend für die Hyaluron-Therapie.</p>
    </div>
    <div class="text-col text-col--two">
      <p>Mittels kleinster Injektionen wird die Faltenregion<br>mit Hyaluron unterfüllt und somit geglättet. Das<br>Ergebnis ist sofort sichtbar, weitere Korrekturen<br>können umgehend oder im Verlauf durchgeführt<br>werden.</p>
      <p>Typische Anwendungsgebiete sind die<br>Nasolabialfalte, Glabella, Falten im Bereich von<br>Unterlid, Tränenkanal und Mund-(winkel) sowie<br>das Auffüllen der Lippen bzw. des Lippenbogens<br>(„Lippen-Augmentation“). Da es sich um einen<br>körpereigenen Stoff handelt sind keine nennenswer-<br>ten Risiken zu erwarten. Im Verlauf wird das einge-<br>brachte Hyaluron vom Körper abgebaut, eine<br>Wirkdauer von 6-12 Monaten ist zu erwarten.</p>
    </div>

    <h2 class="heading heading--lumex">Lumex</h2>
    <div class="text-col text-col--three">
      <p>Botulinumtoxin wird in der Medizin zur Therapie<br>von Muskelspasmen eingesetzt und vermindert<br>die Muskeltätigkeit.</p>
      <p>Im ästhetischen Bereich eignet sich dieses<br>Produkt zur Faltentherapie, v.a. im Stirn- und Glabel-<br>labereich sowie bei „Krähenfüßen“. Mittels kleiner<br>und so gut wie schmerzfreier Injektionen werden<br>geringe Mengen in definierte Punkte eingebracht,<br>nach 2-6 Tagen setzt die Wirkung<br>ein und hält für 10-12 Monate an.</p>
      <p>Nach mehrmaligen Behandlungen verlängert<br>sich die Wirkdauer.</p>
    </div>

    <div class="footer-claim">
      <p>„Man kann das Altern verlangsamen - auch ohne schmerzhafte Operation! - sprechen Sie uns an“.</p>
      <p>Ihr Dr. Stefan Duriklem. Lindenauer Str. 118 | 06112 Musterstadt</p>
    </div>
  </div>
</body>
</html>
```